Business Card Design Project

This is the first time we use our new logo. We need a business card that we can use both on our institutional corporate relationships and also that works for our staff that deals with consumers directly.

VELUNDA is a new company dedicated to empower consumers and to provide them with the best choices for specialized health care using the latest telemedicine technology (medicine at a distance via videoconference).

We want to print this cards in high quality materials and process. We will like designs that allow us to use UV spot varnish and other techniques that will differentiate us.

We are including Two different versions of Color logos. In addition we are including white over black background logos. Those can be used replacing the black for a color.

Please note this is the first time we will be creating any corporate materials with our new logo and colors.

Target Market(s)

34+ consumers of medium high and high socioeconomic levels.

Industry/Entity Type

Health

Requirements
Must have
• Our logo on its original colors
Should not have
• Any other graphical element or design that is not our logo

```html
<!DOCTYPE html>
<html lang="en">
<head>
<meta charset="utf-8">
<title>VELUNDA Business Card</title>
<link rel="stylesheet" href="https://fonts.googleapis.com/css2?family=Questrial&display=swap">
<style>
  :root {
    --card-bg: #333333;
    --ink: #ffffff;
    --accent-blue: #2ea6de;
    --accent-teal: #1a9aa0;
    --accent-mid: #2592c4;
    --icon-blue: #1f7fc9;
  }
  html, body {
    margin: 0;
    padding: 0;
    overflow: hidden;
    background: var(--card-bg);
  }
  .card {
    position: relative;
    width: 1200px;
    height: 741px;
    background: var(--card-bg);
    overflow: hidden;
    font-family: "Questrial", "Century Gothic", sans-serif;
    color: var(--ink);
  }
  .rule {
    position: absolute;
    top: 0;
    width: 4px;
    height: 546px;
  }
  .rule--outer { left: 66px; background: var(--accent-blue); }
  .rule--inner { left: 81px; background: var(--accent-teal); }
  .holder-name {
    position: absolute;
    left: 114px;
    top: 414px;
    margin: 0;
    font-weight: 400;
    font-size: 47px;
    line-height: 1;
    letter-spacing: 0.5px;
  }
  .contact {
    position: absolute;
    left: 60px;
    top: 568px;
    margin: 0;
    padding: 0;
    list-style: none;
  }
  .contact__item {
    display: flex;
    align-items: center;
    height: 41px;
    font-size: 28px;
  }
  .contact__icon {
    width: 32px;
    height: 32px;
    margin-right: 22px;
    flex: none;
  }
  .brand-name {
    position: absolute;
    left: 690px;
    width: 510px;
    top: 438px;
    margin: 0;
    text-align: center;
    font-weight: 400;
    font-size: 100px;
    line-height: 1;
    letter-spacing: 4px;
  }
  .stripes {
    position: absolute;
    right: 0;
    top: 636px;
    width: 93px;
  }
  .stripe { height: 4px; margin-bottom: 5px; }
  .stripe--blue { background: var(--accent-blue); }
  .stripe--mid { background: var(--accent-mid); }
  .stripe--teal { background: var(--accent-teal); }
</style>
</head>
<body>
<main class="card">
  <div class="rule rule--outer"></div>
  <div class="rule rule--inner"></div>

  <h1 class="holder-name">Name Surname</h1>

  <ul class="contact">
    <li class="contact__item">
      <svg class="contact__icon" viewBox="0 0 32 32" aria-hidden="true">
        <path d="M16 3 L2 16 H6 V29 H13 V20 H19 V29 H26 V16 H30 Z" fill="var(--icon-blue)"/>
      </svg>
      <span>Address: #456,Marlow Place</span>
    </li>
    <li class="contact__item">
      <svg class="contact__icon" viewBox="0 0 32 32" aria-hidden="true">
        <circle cx="16" cy="16" r="13" fill="none" stroke="var(--icon-blue)" stroke-width="2"/>
        <path d="M11 9 L14 9 L15 13 L13 14.5 Q14.5 18 17.5 19 L19 17 L23 18 L23 21 Q22 23 19 22.5 Q11 20 9.5 12 Q9.5 9.5 11 9 Z" fill="var(--icon-blue)"/>
      </svg>
      <span>121 5550147</span>
    </li>
    <li class="contact__item">
      <svg class="contact__icon" viewBox="0 0 32 32" aria-hidden="true">
        <rect x="3" y="8" width="26" height="17" fill="var(--icon-blue)"/>
        <path d="M3 8 L16 18 L29 8" fill="none" stroke="#ffffff" stroke-width="1.5"/>
      </svg>
      <span>info@velunda.com</span>
    </li>
  </ul>

  <p class="brand-name">VELUNDA</p>

  <div class="stripes">
    <div class="stripe stripe--blue"></div>
    <div class="stripe stripe--mid"></div>
    <div class="stripe stripe--teal"></div>
  </div>
</main>
</body>
</html>
```